TV - business card

Tidewell Vantage is an insurance brokerage firm, inovative, proactive, vigorous, which aims to become the leader of the insurance brokers in Anfrica. We should like to get some designs which should be avoided also in Gray / Metallic for the Administration and Orange / Blue for the Managers (ike in the picture sent). The Blue / Green logo is not the correct one, but the source of the file. Please adjust the color accordingly for the business cards. 1 / Orange / Blue 2 / Gray / Metallic We want something classic but which is transmitted strenght, inovation, modernity and most of all, rapidity. We want something start-up like, very punchy and catching eye remaining profesional at the same time. Name: Delton Ashgrove Function: Managing Director Address: N ° 73/74 Cmt. Bolembe - R / C 2B Esquerda - Bairro Quimbuta - Luanda Tel: (+244) 947 385 619 Email: delton.ashgrove@tidewell-v.com Website: www.tidewell-v. com We want classic in the front and creative, colorfull at the back. The cards will be printed in relief, with very high quality of paper.
Industry/Entity Type
Insurance Broker
Colors
Designer to choose colors to be used in the design.
Look and feel

```html
<!DOCTYPE html>
<html lang="en">
<head>
<meta charset="utf-8">
<title>Tidewell Vantage – Business Card</title>
<link href="https://fonts.googleapis.com/css2?family=Gentium+Book+Plus&family=Noto+Sans:wght@400;700&display=swap" rel="stylesheet">
<style>
  :root {
    --paper: #ffffff;
    --card-light: #cdcdcd;
    --card-dark: #3d3d3d;
    --ink: #3f3f3f;
    --frame-dark: #444444;
    --frame-light: #d0d0d0;
    --orange: #e07f4b;
    --blue: #3a87c8;
  }
  html, body {
    margin: 0;
    padding: 0;
    width: 1031px;
    height: 1200px;
    overflow: hidden;
    background: var(--paper);
  }
  .canvas {
    position: relative;
    width: 1031px;
    height: 1200px;
  }
  .card {
    position: absolute;
    left: 31px;
    width: 964px;
    height: 550px;
    font-family: "Noto Sans", "Segoe UI", sans-serif;
  }
  .card--front { top: 37px; background: var(--card-light); color: var(--ink); }
  .card--back { top: 623px; background: var(--card-dark); }

  .frame {
    position: absolute;
    box-sizing: border-box;
    border: 3px solid var(--frame-dark);
  }
  .frame--outer { left: 26px; top: 28px; width: 910px; height: 493px; }
  .frame--inner { left: 39px; top: 40px; width: 884px; height: 469px; }
  .card--back .frame { border-color: var(--frame-light); }

  .brand-mark {
    position: absolute;
    left: 114px;
    top: 125px;
    width: 260px;
    height: 260px;
    box-sizing: border-box;
    border: 16px solid var(--orange);
    border-radius: 50%;
    display: flex;
    align-items: center;
    justify-content: center;
    text-align: center;
  }
  .brand-mark__name {
    font-weight: 700;
    font-size: 30px;
    line-height: 1.15;
    color: var(--blue);
  }

  .person__name {
    position: absolute;
    left: 466px;
    top: 62px;
    margin: 0;
    font-family: "Gentium Book Plus", Georgia, serif;
    font-weight: 400;
    font-size: 54px;
    line-height: 1;
    color: var(--orange);
  }
  .person__role {
    position: absolute;
    left: 471px;
    top: 121px;
    margin: 0;
    font-size: 22px;
    letter-spacing: 0.5px;
    color: var(--ink);
  }

  .contact {
    position: absolute;
    left: 440px;
    margin: 0;
    padding: 0;
    list-style: none;
  }
  .contact__item {
    position: absolute;
    left: 0;
    display: flex;
    align-items: center;
    width: 480px;
  }
  .contact__icon { width: 48px; height: 48px; flex: none; }
  .contact__text {
    margin-left: 20px;
    font-size: 22px;
    line-height: 28px;
    letter-spacing: 0.5px;
    white-space: nowrap;
  }
  .contact__item--phone { top: 196px; }
  .contact__item--email { top: 261px; }
  .contact__item--address { top: 337px; }

  .website {
    position: absolute;
    left: 0;
    width: 964px;
    top: 466px;
    display: flex;
    justify-content: center;
    align-items: center;
    gap: 12px;
    font-size: 22px;
    letter-spacing: 0.5px;
  }
  .website__accent { color: var(--orange); }
  .website__arrow { width: 36px; height: 14px; }

  .back-brand {
    position: absolute;
    left: 0;
    top: 204px;
    width: 964px;
    display: flex;
    flex-direction: column;
    align-items: center;
  }
  .back-brand__circle {
    width: 92px;
    height: 92px;
    box-sizing: border-box;
    border: 8px solid var(--orange);
    border-radius: 50%;
  }
  .back-brand__name {
    margin-top: 18px;
    font-weight: 700;
    font-size: 27px;
    letter-spacing: 0.5px;
    color: var(--orange);
  }
</style>
</head>
<body>
<div class="canvas">

  <section class="card card--front">
    <div class="frame frame--outer"></div>
    <div class="frame frame--inner"></div>

    <div class="brand-mark">
      <span class="brand-mark__name">Tidewell<br>Vantage</span>
    </div>

    <h1 class="person__name">Delton Ashgrove</h1>
    <p class="person__role">Managing Director</p>

    <ul class="contact">
      <li class="contact__item contact__item--phone">
        <svg class="contact__icon" viewBox="0 0 48 48" aria-hidden="true">
          <path d="M24 4 A20 20 0 1 0 44 24" fill="none" stroke="#e07f4b" stroke-width="2.5"/>
          <path d="M16 14 l5 -1 l3 6 l-3 2 q2 5 7 7 l2 -3 l6 3 l-1 5 q-12 1 -19 -19z" fill="none" stroke="#e07f4b" stroke-width="2" stroke-linejoin="round"/>
        </svg>
        <span class="contact__text">(+244) 947 385 619</span>
      </li>
      <li class="contact__item contact__item--email">
        <svg class="contact__icon" viewBox="0 0 48 48" aria-hidden="true">
          <path d="M24 4 A20 20 0 1 0 44 24" fill="none" stroke="#e07f4b" stroke-width="2.5"/>
          <rect x="14" y="18" width="20" height="13" fill="#e07f4b"/>
          <path d="M14 18 l10 8 l10 -8" fill="none" stroke="#cdcdcd" stroke-width="2"/>
        </svg>
        <span class="contact__text">delton.ashgrove@tidewell-v.com</span>
      </li>
      <li class="contact__item contact__item--address">
        <svg class="contact__icon" viewBox="0 0 48 48" aria-hidden="true">
          <path d="M24 4 A20 20 0 1 0 44 24" fill="none" stroke="#e07f4b" stroke-width="2.5"/>
          <path d="M24 35 q-9 -10 -9 -15 a9 9 0 0 1 18 0 q0 5 -9 15z" fill="none" stroke="#e07f4b" stroke-width="2.2"/>
          <circle cx="24" cy="20" r="3.2" fill="#e07f4b"/>
        </svg>
        <span class="contact__text">N° 73/74 Cmt. Bolembe-R / C 2B<br>Esquerda-Bairro Quimbuta-Luanda</span>
      </li>
    </ul>

    <div class="website">
      <svg class="website__arrow" viewBox="0 0 36 14" aria-hidden="true">
        <path d="M0 5 h22 l-4 -5 l18 7 l-18 7 l4 -5 h-22z" fill="#e07f4b"/>
      </svg>
      <span>www.<span class="website__accent">tidewell-v</span>.com</span>
      <svg class="website__arrow" viewBox="0 0 36 14" aria-hidden="true">
        <path d="M36 5 h-22 l4 -5 l-18 7 l18 7 l-4 -5 h22z" fill="#e07f4b"/>
      </svg>
    </div>
  </section>

  <section class="card card--back">
    <div class="frame frame--outer"></div>
    <div class="frame frame--inner"></div>

    <div class="back-brand">
      <div class="back-brand__circle"></div>
      <span class="back-brand__name">TIDEWELL-VANTAGE</span>
    </div>
  </section>

</div>
</body>
</html>
```